Flyer to promote new Commercial HVAC Preventative Maintenance clients

This flyer will be in the body of emails that will be sent to new, existing, and/or potential commericial buildings HVAC clients. It will have the least amount of words used, but it will convey the point with pertinent pictorial and graphics. It will show the value of a Periodic/Preventative routine maintenance to lower operating costs of their commericial buildings (i.e. office, medical, shopping centers, apartment, warehouse facility, etc.), in the following ways:
1) Reduce monthly power usage,
2) Reduce emergency HVAC service calls,
3) Reduce costly repairs costs,
4) Reduce HVAC down-times and angry tenants,
5) Increases the life expectancy of the existing and/or new HVAC equipment in the building and/or the equipment's' early replacement costs,
6) Reduces tenant's early termination of their lease and law suits against the landlords,
7) Increases tenant's renewal of the lease and agree to pay the increase rental rates,
8) Reduces unhappy customers and increases tenant's productivity,
9) By reducing the landlord's expenses, the value of the property will increase considerably and profitable to sell their holdings, or refinance and keep their holdings with an increased ROI (Return On Investment).

Landlords can not depend on their tenants' obligation to maintain the landlords' major assets, which is their HVAC equipment and systems.

With the periodic maintenance done by one reliable and licensed HVAC company, the will not use different companies that may or may not do the right repair job on their unit and hurt their bottom line and increase HVAC replacement COSTLY rates.

```html
<!DOCTYPE html>
<html lang="en">
<head>
<meta charset="utf-8">
<title>CoolCrest HVAC – Periodic Maintenance</title>
<link rel="stylesheet" href="https://fonts.googleapis.com/css2?family=Bebas+Neue&family=Cabin:wght@400;500&family=Montserrat:wght@400;500;700&display=swap">
<style>
  :root {
    --navy: #1d4a78;
    --navy-top: #17406b;
    --navy-bottom: #15284a;
    --green: #55ab48;
    --green-dark: #4b9a40;
    --ink: #333333;
    --white: #ffffff;
    --footer-blue: #5d7598;
  }
  * { box-sizing: border-box; margin: 0; padding: 0; }
  html, body { width: 667px; height: 1200px; overflow: hidden; background: var(--white); }
  .flyer { position: relative; width: 667px; height: 1200px; font-family: "Montserrat", sans-serif; color: var(--ink); }

  .masthead { position: absolute; top: 0; left: 0; width: 667px; height: 99px; }
  .contact { position: absolute; top: 46px; font-size: 10px; line-height: 15px; }
  .contact strong { display: block; color: var(--green); font-weight: 700; font-size: 10px; }
  .contact-web { left: 27px; }
  .contact-phone { right: 22px; text-align: right; }
  .brand { position: absolute; top: 26px; left: 0; width: 667px; text-align: center;
    font-family: "Bebas Neue", sans-serif; font-size: 46px; line-height: 50px; color: var(--navy); letter-spacing: 0.5px; }

  .photo { position: absolute; }
  .photo-hero { top: 99px; left: 0; width: 667px; height: 316px;
    background: linear-gradient(180deg, #9dbfe2 0%, #b9cfe2 30%, #a9bdd0 55%, #8fa7bd 80%, #b7c1c9 100%); }
  .photo-crew { top: 872px; left: 0; width: 334px; height: 164px;
    background: linear-gradient(160deg, #5c5c5c 0%, #8b8d8f 40%, #3a3633 100%); }
  .photo-roof { top: 872px; left: 334px; width: 333px; height: 164px;
    background: linear-gradient(180deg, #6f9cd0 0%, #a5bfd8 40%, #c9cccd 70%, #9e9e9a 100%); }

  .pitch { position: absolute; top: 428px; left: 0; width: 667px; text-align: center; }
  .pitch h1 { font-size: 17.5px; font-weight: 700; color: var(--navy); line-height: 24px; }
  .pitch p { margin-top: 6px; font-size: 17px; font-weight: 400; line-height: 21px; color: var(--ink); }

  .cta { position: absolute; top: 526px; left: 282px; width: 104px; height: 26px;
    background: var(--green); border-radius: 2px; box-shadow: 0 2px 4px rgba(0,0,0,0.3);
    font-family: "Bebas Neue", sans-serif; font-size: 21px; line-height: 27px; color: var(--white);
    text-align: center; text-decoration: none; }

  .benefits { position: absolute; top: 573px; left: 23px; width: 621px;
    display: grid; grid-template-columns: repeat(3, 196px); grid-auto-rows: 82px; column-gap: 16.5px; row-gap: 15px; list-style: none; }
  .benefit { display: flex; align-items: center; justify-content: center; text-align: center; padding: 0 10px;
    font-family: "Cabin", sans-serif; font-size: 11.6px; line-height: 15px; color: var(--white); }
  .benefit-green { background: linear-gradient(180deg, var(--green) 0%, var(--green-dark) 100%); }
  .benefit-navy { background: linear-gradient(180deg, var(--navy-top) 0%, var(--navy-bottom) 100%); }

  .trust { position: absolute; top: 1056px; left: 0; width: 667px; height: 144px;
    background: linear-gradient(120deg, #6a80a3 0%, var(--footer-blue) 50%, #4d6790 100%); color: var(--white); }
  .trust-title { position: absolute; top: 28px; left: 45px; font-size: 17.5px; font-weight: 400; }
  .trust-title b { font-weight: 700; }
  .trust-rule { position: absolute; top: 27px; left: 299px; width: 3px; height: 92px; background: var(--green); }
  .trust-copy { position: absolute; top: 20px; left: 333px; width: 330px; font-size: 15.6px; font-weight: 500; line-height: 25.5px; }
</style>
</head>
<body>
<main class="flyer">
  <header class="masthead">
    <div class="contact contact-web">Visit Website<strong>www.coolcresthvac.com</strong></div>
    <div class="brand">CoolCrest HVAC</div>
    <div class="contact contact-phone">Call Us Today<strong>000 555 0142 800</strong></div>
  </header>

  <div class="photo photo-hero" role="img" aria-label="Rooftop commercial HVAC condenser units with ducting under a blue sky"></div>

  <section class="pitch">
    <h1>Unlock Savings, Ensure Sustainability</h1>
    <p>Elevate Your Commercial Building's Efficiency<br>with Periodic Maintenance!</p>
  </section>

  <a class="cta" href="#">Learn More</a>

  <ul class="benefits">
    <li class="benefit benefit-green">Reduce monthly power usage</li>
    <li class="benefit benefit-navy">Reduce emergency<br>HVAC service calls</li>
    <li class="benefit benefit-green">Reduce costly<br>repairs costs</li>
    <li class="benefit benefit-navy">Reduce HVAC down-times<br>and angry tenants</li>
    <li class="benefit benefit-green">Boosts HVAC lifespan of the existing and/or new HVAC equipment, Cut early replacement Costs!</li>
    <li class="benefit benefit-navy">Reduces tenant's early termination of their lease and law suits against the landlords</li>
    <li class="benefit benefit-green">Increases tenant's renewal of the lease and agree to pay the increase rental rates</li>
    <li class="benefit benefit-navy">Reduces unhappy customers and increases tenant's productivity</li>
    <li class="benefit benefit-green">Lower Expenses,<br>Increase Property Value,<br>Maximize ROI<br>(Return On Investment)</li>
  </ul>

  <div class="photo photo-crew" role="img" aria-label="Technicians in hard hats servicing a row of HVAC fan units, seen from above"></div>
  <div class="photo photo-roof" role="img" aria-label="Commercial rooftop with ventilation stack, ducting and stairs"></div>

  <footer class="trust" role="group" aria-label="Trusted partners">
    <h2 class="trust-title"><b>Our Trusted</b> Partners</h2>
    <div class="trust-rule"></div>
    <p class="trust-copy">Trust a Reliable, Licensed HVAC Partner for Periodic Maintenance. Avoid Costly Repairs and Ensure Longevity.</p>
  </footer>
</main>
</body>
</html>
```